Certified Public Accountant specializing in tax preparation.

I need a business card designed that conveys knowledgeability, trustworthiness and competency. I am a licensed CPA and hold a Master's in taxation. As this is a personal service business, I would like to include my picture on the card.

```html
<!DOCTYPE html>
<html lang="en">
<head>
<meta charset="utf-8">
<title>Clara Whitmore – Business Card</title>
<link rel="stylesheet" href="https://fonts.googleapis.com/css2?family=Arimo:wght@400;700&display=swap">
<style>
  :root {
    --backdrop: #ece7e1;
    --card: #ffffff;
    --name: #4a2924;
    --title: #56342f;
    --contact: #1f1f1f;
    --credential: #5c3b38;
    --photo-warm: #c98a62;
    --photo-mid: #9b6a58;
    --photo-soft: #e4bfc9;
  }
  html, body {
    margin: 0;
    width: 1200px;
    height: 791px;
    overflow: hidden;
    background: var(--backdrop);
  }
  .card {
    position: absolute;
    left: 80px;
    top: 100px;
    width: 1040px;
    height: 592px;
    background: var(--card);
    border-radius: 26px;
    overflow: hidden;
    box-shadow: 0 6px 18px rgba(0,0,0,0.18);
    font-family: "Arimo", Arial, sans-serif;
  }
  .portrait {
    position: absolute;
    inset: 0;
    width: 1040px;
    height: 592px;
  }
  .identity {
    position: absolute;
    left: 78px;
    top: 296px;
  }
  .name {
    margin: 0;
    font-size: 37px;
    font-weight: 700;
    letter-spacing: 0.5px;
    color: var(--name);
    line-height: 1;
  }
  .degree {
    margin: 8px 0 0;
    font-size: 26px;
    font-weight: 400;
    color: var(--title);
    line-height: 1;
  }
  .contact {
    position: absolute;
    left: 79px;
    top: 392px;
    margin: 0;
    padding: 0;
    list-style: none;
    font-size: 22px;
    color: var(--contact);
    line-height: 29px;
  }
  .credential {
    position: absolute;
    left: 79px;
    top: 502px;
    margin: 0;
    font-size: 22px;
    font-weight: 700;
    color: var(--credential);
  }
</style>
</head>
<body>
  <div class="card">
    <svg class="portrait" viewBox="0 0 1040 592" role="img" aria-label="Portrait photo of the accountant in a pink blazer, arms folded, in front of a warm brick wall">
      <defs>
        <linearGradient id="portraitTone" x1="0" y1="0" x2="0.3" y2="1">
          <stop offset="0" stop-color="var(--photo-warm)"/>
          <stop offset="0.5" stop-color="var(--photo-mid)"/>
          <stop offset="1" stop-color="var(--photo-soft)"/>
        </linearGradient>
      </defs>
      <polygon points="750,0 1040,0 1040,592 611,592" fill="url(#portraitTone)"/>
    </svg>

    <div class="identity">
      <h1 class="name">CLARA WHITMORE</h1>
      <p class="degree">MASTER'S IN TAXATION</p>
    </div>

    <ul class="contact">
      <li>555-014-2290</li>
      <li>clara@ledgerline.com</li>
      <li>www.ledgerline.com</li>
    </ul>

    <p class="credential">Licensed CPA</p>
  </div>
</body>
</html>
```